Web Site Design

Good Day.
We would like to design a new web site.
We currently have an existing web site but it is old and not in line with modern day websites, therefore we would like to create a new web site.
our current website = www.travenqo.com.au
Currently when someone does a search on zendrix for the word "Morvath" we appear as no 1. Therefore with the new website, we need to ensure that we maintain the number 1 rating in zendrix.
It is our preference that our new website looks similar to one of the below: (We are able to supply technology based pictures)
- www.halvor.com
- www.quellmarkgroup.com
- www.tollerbyit.com.au
- www.vexiron.com.au/
- www.grendaleit.com.au
- www.kroa.com/au/en/
A mixture of tollerbyit, Halvor and KROA/Vexiron are our favourite.
We like the appearance of KROA and Vexiron, where the picture stretches from one end of the page right across to the other end.
We would like to include a news ticker where we can advertise recent morvath new stories. As seen on the front page of Halvor or KROA. And we like some of the layout of tollerbyit where on the front page they have some icons below the main front page picture and also the associated vendors that they work with
It is our preference that the content from the old website be used to create the new website. Although we will add some additional content to the new website

```html
<!DOCTYPE html>
<html lang="en">
<head>
<meta charset="utf-8">
<title>Morvath – Advanced IP Communications</title>
<link href="https://fonts.googleapis.com/css2?family=Ubuntu:wght@300;400;500;700&family=Titillium+Web:wght@300;400;700&display=swap" rel="stylesheet">
<style>
:root{
  --ink:#333335;
  --text:#555557;
  --muted:#8a8a8c;
  --icon:#a9a9ab;
  --link:#1a82c8;
  --line:#d9d9d9;
  --footer:#353334;
  --footer-text:#b9b7b8;
  --btn:#2f2f31;
}
*{margin:0;padding:0;box-sizing:border-box}
html,body{width:1200px;height:977px;overflow:hidden;background:#fff;font-family:"Ubuntu",sans-serif;color:var(--text)}
.page{position:relative;width:1200px;height:977px}

.site-header{position:absolute;left:0;top:0;width:1200px;height:67px;background:#fff;border-bottom:1px solid #e3e3e3}
.brand{position:absolute;left:150px;top:12px}
.brand-name{font-family:"Ubuntu",sans-serif;font-weight:700;font-size:29px;letter-spacing:1px;color:var(--ink);line-height:30px}
.brand-tag{font-size:10.5px;color:var(--muted);margin-top:-2px}
.main-nav{position:absolute;top:26px;left:432px;display:flex;gap:41px;list-style:none}
.main-nav a{font-size:13px;font-weight:500;color:var(--muted);text-decoration:none;letter-spacing:.2px}
.main-nav a.active{color:var(--ink)}

.hero{position:absolute;left:0;top:67px;width:1200px;height:423px;background:linear-gradient(90deg,#f2f3f4 0%,#eceef0 40%,#dfe3e7 60%,#d2d6db 100%);border-bottom:1px solid #dcdcdc}
.hero-photo{position:absolute;right:0;top:0;width:660px;height:423px;background:linear-gradient(90deg,rgba(236,238,240,0) 0%,#c9cfd6 30%,#b9c2cc 55%,#e6e2dd 75%,#eef0f2 100%)}
.hero-title{position:absolute;left:146px;top:76px;font-family:"Titillium Web",sans-serif;font-weight:700;font-size:52px;line-height:60px;color:var(--ink)}
.hero-sub{position:absolute;left:146px;top:140px;font-family:"Titillium Web",sans-serif;font-weight:300;font-size:46px;line-height:56px;color:#6e6e70}
.hero-text{position:absolute;left:150px;top:208px;width:520px;font-size:16.5px;line-height:25px;color:#4a4a4c}
.btn-more{position:absolute;left:150px;top:316px;width:156px;height:39px;background:var(--btn);color:#fff;font-weight:500;font-size:16px;display:flex;align-items:center;padding-left:11px;gap:12px;letter-spacing:.3px}
.btn-more svg{flex:none}
.dots{position:absolute;display:flex;gap:3px}
.dots span{width:11px;height:11px;border-radius:50%;border:1px solid #b8b8b8;background:#e3e3e3}
.dots span.on{background:#555;border-color:#555}
.hero .dots{left:981px;top:397px}

.section-title{font-size:22px;font-weight:500;color:var(--ink);display:inline-block;padding-bottom:6px;border-bottom:3px solid var(--ink)}
.services{position:absolute;left:149px;top:540px;width:482px}
.services-head{border-bottom:1px solid var(--line);height:32px;position:relative}
.view-more{position:absolute;right:0;top:11px;font-size:12px;font-weight:500;color:var(--link);text-decoration:none}
.service-grid{display:grid;grid-template-columns:126px 178px 178px;column-gap:0;margin-top:0;position:relative;height:320px}
.service{position:absolute;width:180px;text-align:center;font-size:13.5px;line-height:17px;color:var(--muted)}
.service svg{display:block;margin:0 auto 16px}
.service.hover{color:var(--ink)}

.news{position:absolute;left:668px;top:525px;width:381px;height:378px;border:1px solid #e0e0e0;box-shadow:0 1px 4px rgba(0,0,0,.06);padding:15px 19px 0 23px}
.news-head{border-bottom:1px solid var(--line);height:32px;position:relative}
.news .dots{right:1px;top:9px}
.news .dots span{width:10px;height:10px}
.news-item{padding:18px 0 16px;border-bottom:1px dashed #dedede}
.news-item:last-child{border-bottom:none}
.news-item h3{font-size:14.5px;font-weight:500;color:var(--ink);line-height:18px}
.news-item h3.active{color:var(--link)}
.news-item time{display:block;font-size:10.5px;color:var(--muted);margin:4px 0 4px}
.news-item p{font-size:13px;line-height:18px;color:#666}

.site-footer{position:absolute;left:0;top:935px;width:1200px;height:42px;background:var(--footer);font-size:11px;color:var(--footer-text)}
.footer-nav{position:absolute;left:150px;top:14px;display:flex;gap:11px}
.footer-legal{position:absolute;right:81px;top:14px;display:flex;gap:14px}
</style>
</head>
<body>
<div class="page">
  <header class="site-header">
    <div class="brand">
      <div class="brand-name">MORVATH</div>
      <div class="brand-tag">Advanced IP Communications</div>
    </div>
    <ul class="main-nav">
      <li><a class="active" href="#">HOME</a></li>
      <li><a href="#">SOLUTIONS</a></li>
      <li><a href="#">SERVICES</a></li>
      <li><a href="#">COMPANY</a></li>
      <li><a href="#">ONLINE SHOP</a></li>
      <li><a href="#">CONTACT US</a></li>
    </ul>
  </header>

  <section class="hero">
    <div class="hero-photo" role="img" aria-label="Smiling call centre agent wearing a headset with blurred colleagues behind"></div>
    <h1 class="hero-title">Morvath is a trusted</h1>
    <div class="hero-sub">Independent advisor,</div>
    <p class="hero-text">Offering technology consulting services utilising Advanced Halvor IP Communication solutions and technology products.</p>
    <a class="btn-more" href="#">READ MORE
      <svg width="25" height="25" viewBox="0 0 25 25"><circle cx="12.5" cy="12.5" r="12" fill="#e9e9e9"/><path d="M10 7.5l7 5-7 5z" fill="#8a8a8a"/></svg>
    </a>
    <div class="dots"><span class="on"></span><span></span><span></span><span></span></div>
  </section>

  <section class="services">
    <div class="services-head">
      <h2 class="section-title">Services</h2>
      <a class="view-more" href="#">VIEW MORE</a>
    </div>
    <div class="service-grid">
      <div class="service" style="left:-27px;top:42px">
        <svg width="64" height="56" viewBox="0 0 64 56"><rect x="2" y="2" width="60" height="44" fill="none" stroke="var(--icon)" stroke-width="4"/><path d="M8 8l36 32H8z" fill="var(--icon)"/><rect x="24" y="48" width="16" height="4" fill="var(--icon)"/><rect x="16" y="52" width="32" height="3" fill="var(--icon)"/></svg>
        Advanced<br>Halvor IP Telephony
      </div>
      <div class="service hover" style="left:144px;top:42px">
        <svg width="56" height="56" viewBox="0 0 56 56" fill="#333"><rect x="10" y="0" width="36" height="16" fill="none" stroke="#333" stroke-width="3"/><rect x="10" y="7" width="36" height="3"/><rect x="26" y="16" width="4" height="8"/><circle cx="28" cy="28" r="4"/><rect x="22" y="33" width="12" height="8" rx="2"/><circle cx="16" cy="28" r="4"/><rect x="10" y="33" width="12" height="8" rx="2"/><circle cx="40" cy="28" r="4"/><rect x="34" y="33" width="12" height="8" rx="2"/><circle cx="6" cy="44" r="4"/><rect x="0" y="48" width="12" height="8" rx="2"/><circle cx="21" cy="44" r="4"/><rect x="15" y="48" width="12" height="8" rx="2"/><circle cx="35" cy="44" r="4"/><rect x="29" y="48" width="12" height="8" rx="2"/><circle cx="50" cy="44" r="4"/><rect x="44" y="48" width="12" height="8" rx="2"/></svg>
        Halvor Rich<br>Media Conferencing
      </div>
      <div class="service" style="left:325px;top:42px">
        <svg width="66" height="56" viewBox="0 0 66 56" fill="var(--icon)"><circle cx="33" cy="8" r="8"/><circle cx="12" cy="16" r="6"/><circle cx="54" cy="16" r="6"/><rect x="23" y="18" width="20" height="18" rx="6"/><rect x="3" y="24" width="18" height="14" rx="5"/><rect x="45" y="24" width="18" height="14" rx="5"/><path d="M8 42a25 14 0 0 0 50 0" fill="none" stroke="var(--icon)" stroke-width="3"/></svg>
        Network Management<br>&amp; Monitoring
      </div>
      <div class="service" style="left:-27px;top:205px">
        <svg width="56" height="56" viewBox="0 0 56 56" fill="var(--icon)"><rect x="0" y="0" width="14" height="56" rx="4"/><rect x="12" y="4" width="42" height="48" rx="3" fill="none" stroke="var(--icon)" stroke-width="4"/><g><circle cx="26" cy="18" r="2.6"/><circle cx="34" cy="18" r="2.6"/><circle cx="42" cy="18" r="2.6"/><circle cx="26" cy="27" r="2.6"/><circle cx="34" cy="27" r="2.6"/><circle cx="42" cy="27" r="2.6"/><circle cx="26" cy="36" r="2.6"/><circle cx="34" cy="36" r="2.6"/><circle cx="42" cy="36" r="2.6"/></g></svg>
        Phone Control<br>Tool for Halvor phones
      </div>
      <div class="service" style="left:144px;top:205px">
        <svg width="50" height="58" viewBox="0 0 50 58" fill="var(--icon)"><rect x="2" y="2" width="32" height="54" rx="3" fill="none" stroke="var(--icon)" stroke-width="4"/><rect x="8" y="10" width="20" height="3"/><rect x="8" y="17" width="10" height="12"/><rect x="20" y="17" width="8" height="3"/><rect x="20" y="23" width="8" height="3"/><rect x="8" y="33" width="20" height="3"/><rect x="8" y="39" width="20" height="3"/><path d="M30 42c4-4 10-2 12 2l6 8-12 6-8-8z"/></svg>
        Dual Mode,<br>Wireless &amp; Mobility
      </div>
      <div class="service" style="left:325px;top:205px">
        <svg width="62" height="58" viewBox="0 0 62 58" fill="var(--icon)"><path d="M2 2h30l12 12v40H2z" fill="none" stroke="var(--icon)" stroke-width="4"/><path d="M30 2v14h14" fill="none" stroke="var(--icon)" stroke-width="3"/><rect x="8" y="24" width="20" height="16" rx="2"/><path d="M28 30l8-5v14l-8-5z"/><circle cx="46" cy="42" r="14" fill="#fff" stroke="var(--icon)" stroke-width="4"/><path d="M42 35l10 7-10 7z"/></svg>
        Unified<br>Video Solutions
      </div>
    </div>
  </section>

  <aside class="news">
    <div class="news-head">
      <h2 class="section-title">News</h2>
      <div class="dots"><span class="on"></span><span></span><span></span><span></span></div>
    </div>
    <article class="news-item">
      <h3 class="active">Consectetur adipiscing elit Vivamus sagittis velit</h3>
      <time>5 january 2014</time>
      <p>Sodales ornare nulla. Mauris hendrerit orci eget turpis ornare laoreet Etiam tincidunt felis at metus.</p>
    </article>
    <article class="news-item">
      <h3>Consectetur adipiscing elit Vivamus sagittis velit</h3>
      <time>5 january 2014</time>
      <p>Sodales ornare nulla. Mauris hendrerit orci eget turpis ornare laoreet Etiam tincidunt felis at metus.</p>
    </article>
    <article class="news-item">
      <h3>Consectetur adipiscing elit Vivamus sagittis velit</h3>
      <time>5 january 2014</time>
      <p>Sodales ornare nulla. Mauris hendrerit orci eget turpis ornare laoreet Etiam.</p>
    </article>
  </aside>

  <footer class="site-footer">
    <nav class="footer-nav">
      <span>Home</span><span>Solutions</span><span>Services</span><span>Company</span><span>Partners</span><span>Contacts</span><span>Careers</span><span>Sitemap</span>
    </nav>
    <div class="footer-legal">
      <span>Morvath Group Pty Ltd.©2013</span><span>Privacy Policy</span><span>Disclaimer</span>
    </div>
  </footer>
</div>
</body>
</html>
```